Business Card for Makeup Artist

I need a business card designed for my makeup and hair artistry business which is primarily events and weddings focused. The card needs to be sleek, simple, stylish and appealing to women. I would prefer a white background but open to suggestions also. I also love the marble background look. I have attached some example pics. It needs to be a double sided card with logo and/or design on one side and contact details in the centre of the card on the other side. NO LOGO ON BACK. Examples attached.

Target Market(s)

Females age 14-55

Industry/Entity Type

Business

Contact Information for Business Card

Nora Vint
Principal Makeup Artist
P: 0413 925 214
E: nora@lumirabeauty.com.au
W: www.lumirabeauty.com.au

Requirements
Should not have
• No yellow, green, red or blue in the design.

```html
<!DOCTYPE html>
<html lang="en">
<head>
<meta charset="utf-8">
<title>Lumira Makeup Artistry – Business Card</title>
<link rel="stylesheet" href="https://fonts.googleapis.com/css2?family=Open+Sans:wght@400;600;700&display=swap">
<style>
  :root {
    --backdrop: #2e3034;
    --card-white: #ffffff;
    --card-pink: #f463d3;
    --ink-grey: #5b5b5d;
    --ink-white: #ffffff;
    --card-w: 600px;
    --card-h: 343px;
  }
  * { margin: 0; padding: 0; box-sizing: border-box; }
  html, body {
    width: 1200px;
    height: 864px;
    overflow: hidden;
    background: var(--backdrop);
    font-family: "Open Sans", Arial, sans-serif;
  }
  .canvas {
    position: relative;
    width: 1200px;
    height: 864px;
  }
  .card {
    position: absolute;
    left: 300px;
    width: var(--card-w);
    height: var(--card-h);
    display: flex;
    flex-direction: column;
    align-items: center;
    justify-content: center;
    text-align: center;
    box-shadow: 0 12px 30px rgba(0, 0, 0, 0.35);
  }
  .card--front {
    top: 64px;
    background: var(--card-white);
    color: var(--ink-grey);
  }
  .card--back {
    top: 457px;
    background: var(--card-pink);
    color: var(--ink-white);
  }
  .brand-name {
    font-size: 64px;
    font-weight: 400;
    letter-spacing: 6px;
    line-height: 1;
    color: var(--ink-grey);
  }
  .brand-tagline {
    margin-top: 10px;
    margin-left: 70px;
    font-size: 21px;
    font-weight: 400;
    letter-spacing: 1px;
    color: var(--ink-grey);
  }
  .person-name {
    font-size: 19px;
    font-weight: 700;
    letter-spacing: 0.5px;
    text-transform: uppercase;
  }
  .person-role {
    font-size: 14px;
    font-weight: 400;
    margin-top: 1px;
  }
  .divider {
    width: 168px;
    margin: 12px 0 16px;
    border: 0;
    border-top: 1px dashed var(--ink-white);
  }
  .contact-list {
    list-style: none;
    font-size: 15px;
    line-height: 1.45;
  }
  .contact-label { font-weight: 700; }
</style>
</head>
<body>
<main class="canvas">
  <section class="card card--front" aria-label="Card front">
    <div class="brand-name">Lumira</div>
    <div class="brand-tagline">MAKEUP ARTISTRY</div>
  </section>

  <section class="card card--back" aria-label="Card back">
    <h1 class="person-name">Nora Vint</h1>
    <p class="person-role">Principal Makeup Artist</p>
    <hr class="divider">
    <ul class="contact-list">
      <li><span class="contact-label">Phone :</span> 0413 925 214</li>
      <li><span class="contact-label">Email :</span> nora@lumirabeauty.com.au</li>
      <li><span class="contact-label">Website :</span> www.lumirabeauty.com.au</li>
    </ul>
  </section>
</main>
</body>
</html>
```